Mardi Gras 2013 Design Project

We have a design with elements that we want to retain. However, we need to take what we have and give it a creative BOOST!

Requirements
Must have
• Colors must stay, "KL" logo must stay,
Copy must remain (except - "Requests Your Presence" and small copy in bottom right corner);
Seal must remain, "9th Annual Mardi Gras Ball" frame text can be modified but should resemble;
Gotham font to remain
Nice to have
• Any new Mardi Gras element - like a mask or beads - but can not over shadow copy

```html
<!DOCTYPE html>
<html lang="en">
<head>
<meta charset="utf-8">
<title>9th Annual Mardi Gras Ball</title>
<link rel="stylesheet" href="https://fonts.googleapis.com/css2?family=Montserrat:ital,wght@0,700;0,800;1,700;1,800;1,900&display=swap">
<style>
  :root {
    --frame-green: #3f9c4c;
    --ground-purple: #503a8e;
    --deep-purple: #3a2470;
    --gold: #e3a63c;
    --green: #3fae55;
    --lilac: #9c62d6;
    --mask-light: #7a56c2;
  }
  html, body { margin: 0; padding: 0; overflow: hidden; }
  body { width: 900px; height: 1200px; }
  .poster {
    position: relative;
    width: 900px; height: 1200px;
    box-sizing: border-box;
    border: 18px solid var(--frame-green);
    background: var(--ground-purple);
    overflow: hidden;
    font-family: "Montserrat", Arial, sans-serif;
  }
  .mask-art {
    position: absolute; left: 250px; top: -20px; width: 540px; height: 400px; z-index: 0;
    border-radius: 48% 52% 45% 55% / 55% 55% 45% 45%;
    background: radial-gradient(ellipse at 50% 40%, var(--mask-light) 0%, #5c3fa4 55%, rgba(80,58,142,0) 75%);
  }
  .monogram {
    position: absolute; left: 34px; top: 38px; z-index: 2;
    width: 170px; height: 140px;
    display: flex; align-items: center; justify-content: center; gap: 10px;
    color: var(--gold); font-weight: 800; font-size: 82px; letter-spacing: 2px;
  }
  .monogram-dot { width: 18px; height: 18px; border-radius: 50%; background: var(--gold); }
  .host {
    position: absolute; right: 22px; top: 46px; width: 380px; z-index: 2;
    text-align: center; color: var(--gold);
    font-weight: 700; font-size: 24px; line-height: 1.3; margin: 0;
  }
  .title { position: absolute; inset: 0; margin: 0; z-index: 1; }
  .outline {
    --stroke: var(--gold);
    position: absolute; margin: 0; line-height: 1; white-space: nowrap;
    font-style: italic; font-weight: 900;
    color: var(--ground-purple);
    text-shadow:
      2px 0 0 var(--stroke), -2px 0 0 var(--stroke),
      0 2px 0 var(--stroke), 0 -2px 0 var(--stroke),
      1.5px 1.5px 0 var(--stroke), -1.5px -1.5px 0 var(--stroke),
      1.5px -1.5px 0 var(--stroke), -1.5px 1.5px 0 var(--stroke);
  }
  .title-number { --stroke: var(--green); left: 305px; top: 262px; font-size: 265px; letter-spacing: -6px; }
  .title-number sup { font-size: 160px; vertical-align: 0; letter-spacing: -2px; }
  .title-annual { left: 252px; top: 497px; font-size: 82px; letter-spacing: 3px; }
  .title-mardi { --stroke: var(--lilac); left: 204px; top: 553px; font-size: 126px; }
  .title-gras { --stroke: var(--green); left: 222px; top: 660px; font-size: 126px; letter-spacing: 14px; }
  .title-ball { left: 258px; top: 756px; font-size: 124px; letter-spacing: 12px; }
  .seal {
    position: absolute; left: 48px; top: 862px; width: 206px; height: 206px; z-index: 2;
    border-radius: 50%; background: var(--gold);
    display: flex; align-items: center; justify-content: center;
    color: var(--deep-purple); font-weight: 800; font-size: 22px; text-align: center; line-height: 1.2;
  }
  .block { position: absolute; left: 0; right: 0; text-align: center; margin: 0; z-index: 2; }
  .details { font-style: italic; font-weight: 800; }
  .day { top: 902px; right: 10px; color: var(--gold); font-size: 30px; }
  .date { top: 938px; right: 10px; color: var(--green); font-size: 32px; }
  .time { top: 976px; right: 10px; color: var(--lilac); font-size: 30px; }
  .venue { top: 1019px; right: 10px; color: var(--gold); font-size: 24px; line-height: 1.26; }
  .street { top: 1092px; right: 10px; color: var(--green); font-size: 25px; }
  .city { top: 1121px; right: 10px; color: var(--green); font-size: 33px; }
</style>
</head>
<body>
<main class="poster">
  <div class="mask-art" role="img" aria-label="Illustration of a purple Mardi Gras masquerade mask on a stick with ribbons"></div>

  <div class="monogram"><span>KL</span><span class="monogram-dot"></span></div>
  <p class="host">THE ASSOCIATION OF<br>KINGSLEY LANE ALUMNI</p>

  <h1 class="title" aria-label="9th Annual Mardi Gras Ball">
    <span class="outline title-number">9<sup>th</sup></span>
    <span class="outline title-annual">ANNUAL</span>
    <span class="outline title-mardi">MARDI</span>
    <span class="outline title-gras">GRAS</span>
    <span class="outline title-ball">BALL</span>
  </h1>

  <div class="seal">KINGSLEY<br>LANE</div>

  <p class="block details day">SATURDAY</p>
  <p class="block details date">JANUARY 26, 2013</p>
  <p class="block details time">7PM - 12AM</p>
  <p class="block details venue">PEACHTREE GRAND<br>EVENT CENTER</p>
  <p class="block details street">1450 GRAND HALL PARKWAY</p>
  <p class="block details city">ATLANTA, GEORGIA</p>
</main>
</body>
</html>
```